Business cards design on a high standard

We advise clients on insurance and financial matters, since these clients pay for our advice, the design should have a high standard. Our logo should be included. From the colors we are open for everything.

Colors

Designer to choose colors to be used in the design.

```html
<!DOCTYPE html>
<html lang="en">
<head>
<meta charset="utf-8">
<title>Alpine Counsel – Business Cards</title>
<link rel="stylesheet" href="https://fonts.googleapis.com/css2?family=Open+Sans:ital,wght@0,400;0,600;0,800;1,400&display=swap">
<style>
  :root {
    --bg: #e6e6e8;
    --card-white: #ffffff;
    --card-black: #1d1d1f;
    --brand-red: #e41e26;
    --brand-grey: #9a9ba0;
    --text-dark: #3a3a3c;
    --mark-dark: #2c2c2e;
  }
  * { margin: 0; padding: 0; box-sizing: border-box; }
  html, body { width: 1200px; height: 900px; overflow: hidden; }
  body {
    background: var(--bg);
    font-family: "Open Sans", sans-serif;
    position: relative;
  }
  .card {
    position: absolute;
    left: 250px;
    width: 700px;
    height: 400px;
    overflow: hidden;
    box-shadow: 0 6px 18px rgba(0,0,0,0.18);
  }
  .card--back { top: 40px; background: var(--card-black); }
  .card--front { top: 460px; background: var(--card-white); }

  .back-wordmark {
    position: absolute;
    left: 0; right: 0; top: 160px;
    text-align: center;
    font-family: "Open Sans", sans-serif;
    font-weight: 800;
    font-size: 58px;
    letter-spacing: 2px;
    color: var(--mark-dark);
    text-transform: uppercase;
  }

  .front-wordmark {
    position: absolute;
    left: 60px; top: 138px;
    font-family: "Open Sans", sans-serif;
    font-weight: 800;
    font-size: 40px;
    line-height: 1.05;
    color: var(--brand-red);
    text-transform: uppercase;
  }
  .divider {
    position: absolute;
    left: 370px; top: 100px;
    width: 2px; height: 180px;
    background: var(--brand-red);
  }
  .contact {
    position: absolute;
    left: 392px; top: 100px;
    color: var(--text-dark);
    font-size: 19px;
    line-height: 1.3;
  }
  .contact__name {
    color: var(--brand-red);
    font-weight: 800;
    font-size: 24px;
    text-transform: uppercase;
    letter-spacing: 0.5px;
    line-height: 1.1;
  }
  .contact__role { font-size: 19px; margin-bottom: 14px; }
  .contact__address { margin-bottom: 10px; }
  .contact__line { display: flex; align-items: center; gap: 8px; }
  .contact__line svg { flex: none; }

  .wave { position: absolute; left: 0; bottom: 0; }
  .website {
    position: absolute;
    left: 48px; top: 333px;
    color: #ffffff;
    font-style: italic;
    font-size: 19px;
    transform: rotate(3deg);
    transform-origin: left center;
  }
</style>
</head>
<body>

<section class="card card--back" aria-label="Card back">
  <div class="back-wordmark">Alpine Counsel</div>
</section>

<section class="card card--front" aria-label="Card front">
  <div class="front-wordmark">Alpine<br>Counsel</div>
  <div class="divider"></div>

  <div class="contact">
    <div class="contact__name">Daniel Harrow</div>
    <div class="contact__role">President</div>
    <div class="contact__address">4820 Marina Crest Drive<br>Seacliff CA 90000</div>
    <div class="contact__line">
      <svg width="16" height="16" viewBox="0 0 24 24" aria-hidden="true">
        <path fill="#e41e26" d="M6.6 10.8a15.1 15.1 0 0 0 6.6 6.6l2.2-2.2a1 1 0 0 1 1-.25 11.4 11.4 0 0 0 3.6.57 1 1 0 0 1 1 1V20a1 1 0 0 1-1 1A17 17 0 0 1 3 4a1 1 0 0 1 1-1h3.5a1 1 0 0 1 1 1c0 1.25.2 2.46.57 3.6a1 1 0 0 1-.25 1z"/>
      </svg>
      <span>555-010-4821</span>
    </div>
    <div class="contact__line">
      <svg width="16" height="12" viewBox="0 0 24 18" aria-hidden="true">
        <path fill="#e41e26" d="M0 0h24v2.5L12 10 0 2.5z M0 5l12 7.5L24 5v13H0z"/>
      </svg>
      <span>daniel@alpinecounsel.com</span>
    </div>
  </div>

  <svg class="wave" width="700" height="400" viewBox="0 0 700 400" aria-hidden="true">
    <path d="M0,300 C160,278 320,300 470,345" fill="none" stroke="#9a9ba0" stroke-width="7"/>
    <path d="M520,362 C590,380 650,378 700,368" fill="none" stroke="#9a9ba0" stroke-width="7"/>
    <path d="M0,314 C160,296 320,318 460,360 C560,390 640,390 700,380 L700,400 L0,400 Z" fill="#e41e26"/>
  </svg>
  <div class="website">www.alpinecounsel.com</div>
</section>

</body>
</html>
```